Employment Agency Website Design

We are working with an employment agency in California.

Some sites to use for content/competitors and inspiration:

https://www.travinmoor.example/us/en
https://www.pelkoworksusa.example
https://www.dunmarhire.example
https://www.vantriga.example/en
https://www.ombrelusa.example
https://www.quilnstaffing.example

Thank you for taking the time to consider designing a website for us. We are web developers based in Stockton, CA, USA. Most of our projects go through the same process. Understanding this process may help you win a project with us. We custom-code all of our websites in-house. We don’t have any requirements as to what tools you use for your design, but we prefer Figma files. For any design that we label as four-stars, we send it to the client for review. The client picks the final design they want us to use. Once we complete this process, we will continue to show additional clients all the four-star sites and purchase them later. Your designs will have multiple chances to sell. For better chances of success, we ask that you follow these guidelines.

IMAGES:
If you use any images or icons in the design, we ask that you have a link to the asset so we can purchase the image/icon. Most of the designs we submit do not have the customer’s images on them unless they have some great images. Be creative; show us the feeling you are trying to portray with your image choices. Use any royalty-free site you choose. We subscribe to Adobe and mainly use their images, but we can purchase images outside of Adobe. PLEASE NOTE: we will not submit designs to clients with watermarks on the images.

FONTS:
We ask that you identify the fonts used in the design. This can be done in a message if you want. We typically use Google Fonts and Adobe Fonts.

CONTENT:
We're always open to different content and ideas. We often submit designs with stock images so the client can see our vision. We typically take pictures after the website launch to use their images with our vision. Lorem Ipsum is fine for paragraphs, but we ask that you write the headers in correct English. We want to be able to show the vision and identify the sections of the website.

INSPIRATION:
We typically add a couple of links in the brief of websites we like to help you get started in your design.

REVISIONS:
We do not often ask for revisions of the designs unless we see something in the design that may not appeal to the client. If there are slight changes that we want to make, we do that in the development process.

FEEDBACK:
We rarely give feedback on designs during the design process. We are working on many website projects and do not have the time to provide feedback. We usually respond if your request is well thought out and asks specific questions, but a note asking “feedback, please” usually goes unanswered.

```html
<!DOCTYPE html>
<html lang="en">
<head>
<meta charset="utf-8">
<title>Nuvara Talent — Staffing Agency</title>
<link href="https://fonts.googleapis.com/css2?family=Poppins:wght@400;500;600;700&display=swap" rel="stylesheet">
<style>
:root{
  --red:#c8102e;
  --red-dark:#a50d25;
  --ink:#1b1b1b;
  --muted:#555;
  --panel:#efefef;
  --black:#111;
  --white:#fff;
}
*{box-sizing:border-box;margin:0;padding:0}
html,body{width:1200px;height:4768px;overflow:hidden}
body{font-family:"Poppins",Arial,sans-serif;color:var(--ink);background:var(--white);position:relative}
p{font-size:13px;line-height:1.55;color:var(--muted)}
.btn{display:inline-block;background:var(--red);color:var(--white);font-size:11px;font-weight:600;text-transform:uppercase;padding:10px 20px;letter-spacing:.3px;white-space:nowrap}
.btn.dark{background:var(--black)}

/* header */
.site-header{position:absolute;top:0;left:0;width:1200px;height:64px;background:var(--white);display:flex;align-items:center;padding:0 20px;z-index:3}
.brand{display:flex;align-items:center;gap:8px;font-weight:600;font-size:22px;color:var(--ink);white-space:nowrap}
.brand-mark{width:22px;height:22px;background:var(--red)}
.login-group{display:flex;gap:14px;margin-left:80px}
.login-btn{background:var(--red);color:var(--white);font-size:14px;padding:10px 20px;display:flex;align-items:center;gap:8px;white-space:nowrap}
.login-btn i{width:14px;height:14px;border-radius:50%;background:var(--white);display:inline-block}
.main-nav{margin-left:auto;display:flex;gap:28px;font-size:15px;font-weight:500;white-space:nowrap}

/* hero */
.hero{position:absolute;top:0;left:0;width:1200px;height:800px}
.hero-photo{position:absolute;inset:0;background:linear-gradient(100deg,#2b2b2e 0%,#4a4a4f 45%,#8a8580 75%,#b9b2a8 100%)}
.hero-shade{position:absolute;inset:0;background:linear-gradient(90deg,rgba(0,0,0,.55),rgba(0,0,0,.1) 70%)}
.hero-content{position:absolute;left:36px;top:195px;width:520px;color:var(--white)}
.hero-content h1{font-size:62px;line-height:1.2;font-weight:700}
.hero-content p{color:#eee;margin-top:22px;width:380px}
.hero-actions{margin-top:22px;display:flex;gap:20px}
.hero-wedge{position:absolute;bottom:0;left:0}

/* about */
.about{position:absolute;top:940px;left:0;width:1200px;height:400px}
.about-text{position:absolute;left:48px;top:40px;width:440px}
.about-text h2{font-size:44px;font-weight:600;margin-bottom:18px}
.about-text p{margin-bottom:14px}
.about-photo{position:absolute;left:600px;top:-52px;width:560px;height:424px;background:linear-gradient(180deg,#fff 0%,#f2eeea 60%,#e4e0dc 100%)}
.tag-btn{position:absolute;background:var(--red);color:var(--white);font-size:14px;padding:16px 22px;border-radius:6px;white-space:nowrap}

/* how it works */
.how{position:absolute;top:1400px;left:0;width:1200px;text-align:center}
.how h2{font-size:42px;font-weight:600}
.steps{display:flex;justify-content:center;gap:70px;margin-top:50px}
.step{width:300px}
.step svg{display:block;margin:0 auto 14px}
.step h3{font-size:23px;font-weight:500;margin-bottom:6px;white-space:nowrap}
.step p{width:250px;margin:0 auto;font-size:12px;line-height:1.45}

/* feature rows */
.feature{position:absolute;left:0;width:1200px}
.feature-photo{position:absolute;top:0;height:100%;background:linear-gradient(120deg,#3b3a38 0%,#6b6560 45%,#a49a8e 100%)}
.feature-panel{position:absolute;top:0;height:100%;background:var(--panel);padding:36px 40px}
.feature-panel h2{font-size:40px;font-weight:600;line-height:1.2;margin-bottom:28px}
.tick-list{list-style:none}
.tick-list li{display:flex;gap:16px;margin-bottom:20px;align-items:flex-start}
.tick{flex:none;width:32px;height:32px;background:var(--red);display:flex;align-items:center;justify-content:center}
.tick-list p{font-size:13px;color:#444}

/* trending */
.trending{position:absolute;top:3300px;left:0;width:1200px;text-align:center}
.trending h2{font-size:44px;font-weight:600;margin-bottom:36px}
.job-grid{display:grid;grid-template-columns:repeat(4,240px);justify-content:center;column-gap:35px;row-gap:34px}
.job{font-size:22px;font-weight:600;padding-bottom:8px;border-bottom:4px solid var(--red);margin:0 auto;white-space:nowrap}

/* testimonials */
.testimonials{position:absolute;top:3790px;left:0;width:1200px;height:500px;text-align:center}
.testimonials h2{font-size:44px;font-weight:500}
.testimonials .quote{margin:26px auto 18px;display:block}
.testimonials blockquote{width:640px;margin:0 auto;font-size:13px;line-height:1.7;color:var(--muted)}
.client-name{font-weight:600;font-size:15px;margin-top:8px}
.avatar{position:absolute;border-radius:50%;background:radial-gradient(circle,#d9a98e,#8c5a44)}

/* cta band */
.cta-band{position:absolute;top:4320px;left:0;width:1200px;height:100px;background:var(--red);display:flex;justify-content:center;align-items:center;gap:40px}
.cta-btn{width:290px;height:60px;display:flex;align-items:center;justify-content:center;font-size:24px;font-weight:500;text-transform:uppercase;color:var(--white);white-space:nowrap}
.cta-btn.outline{border:2px solid var(--white)}
.cta-btn.solid{background:var(--black)}

/* footer */
.site-footer{position:absolute;top:4420px;left:0;width:1200px;height:348px;background:var(--black);color:var(--white)}
.footer-cols{display:flex;padding:30px 20px 0;gap:40px}
.footer-brand{width:300px}
.footer-brand .brand{color:var(--white)}
.footer-brand p{color:#ccc;margin-top:14px;font-size:13px}
.socials{display:flex;gap:12px;margin-top:18px}
.socials i{width:18px;height:18px;border-radius:50%;background:var(--white);display:block}
.footer-col{width:230px}
.footer-col h4{font-size:20px;font-weight:600;margin-bottom:12px}
.footer-col ul{list-style:none}
.footer-col li{font-size:14px;margin-bottom:10px}
.footer-col li::before{content:"›";margin-right:8px}
.subscribe{width:270px}
.subscribe h4{font-size:20px;font-weight:600;line-height:1.3;margin-bottom:10px}
.subscribe .field{height:44px;background:var(--white);color:#888;font-size:13px;padding:12px}
.subscribe .btn{display:block;text-align:center;margin-top:8px;font-size:14px;padding:12px}
.copyright{position:absolute;bottom:14px;width:100%;text-align:center;font-size:14px;color:#ddd}
</style>
</head>
<body>

<header class="site-header">
  <div class="brand"><span class="brand-mark"></span>Nuvara Talent</div>
  <div class="login-group">
    <span class="login-btn"><i></i>Client Login</span>
    <span class="login-btn"><i></i>Candidate Login</span>
  </div>
  <nav class="main-nav"><span>Talent Seeker</span><span>Employers</span><span>Solutions</span><span>About Us</span><span>Contact</span></nav>
</header>

<section class="hero">
  <div class="hero-photo" role="img" aria-label="Photo of a job interview between a candidate and recruiters in an office"></div>
  <div class="hero-shade"></div>
  <div class="hero-content">
    <h1>Helping Good People Find Good Jobs</h1>
    <p>Lorem ipsum dolor sit amet, consectetur adipiscing elit, sed do eiusmod tempor incididunt.</p>
    <div class="hero-actions"><span class="btn">Find your next job</span><span class="btn dark">Find your next hire</span></div>
  </div>
  <svg class="hero-wedge" width="1200" height="110" viewBox="0 0 1200 110">
    <polygon points="0,40 600,90 1200,40 1200,110 0,110" fill="#fff"/>
    <polygon points="0,18 600,68 1200,18 1200,40 600,90 0,40" fill="#c8102e"/>
  </svg>
</section>

<section class="about">
  <div class="about-text">
    <h2>About Us</h2>
    <p>Lorem ipsum dolor sit amet, consectetur adipiscing elit. Aenean commodo ligula eget dolor. Aenean massa. Cum sociis natoque penatibus et magnis dis parturient montes, nascetur ridiculus mus.</p>
    <p>Donec quam felis, ultricies nec, pellentesque eu, pretium quis, sem. Nulla consequat massa quis enim. Donec pede justo, fringilla vel, aliquet nec, vulputate eget, arcu.</p>
    <span class="btn">Find your next job</span>
  </div>
  <div class="about-photo" role="img" aria-label="Photo of a smiling professional holding a laptop"></div>
  <span class="tag-btn" style="left:975px;top:35px">Looking to Hire</span>
  <span class="tag-btn" style="left:548px;top:165px">Looking for Job</span>
</section>

<section class="how">
  <h2>How It Works</h2>
  <div class="steps">
    <div class="step">
      <svg width="80" height="80" viewBox="0 0 90 90" fill="none" stroke="#c8102e" stroke-width="3"><rect x="18" y="8" width="50" height="70" rx="4"/><circle cx="43" cy="32" r="9"/><path d="M30 56h26M30 66h18"/></svg>
      <h3>Describe your need</h3>
      <p>Lorem ipsum dolor sit amet, consectetur adipiscing elit, sed do eiusmod tempor incididunt.</p>
    </div>
    <div class="step">
      <svg width="80" height="80" viewBox="0 0 90 90" fill="none" stroke="#c8102e" stroke-width="3"><rect x="10" y="24" width="64" height="48" rx="4"/><path d="M32 24v-8h20v8"/><circle cx="58" cy="56" r="12"/><path d="M67 65l12 12"/></svg>
      <h3>Matching candidates</h3>
      <p>Lorem ipsum dolor sit amet, consectetur adipiscing elit, sed do eiusmod tempor incididunt.</p>
    </div>
    <div class="step">
      <svg width="80" height="80" viewBox="0 0 90 90" fill="none" stroke="#c8102e" stroke-width="3"><path d="M6 40l18-18 14 8 12-6 14 6 20 10"/><path d="M24 48l14 14 8-6 10 10 14-14"/><path d="M38 30l-10 14"/></svg>
      <h3>Get Connected</h3>
      <p>Lorem ipsum dolor sit amet, consectetur adipiscing elit, sed do eiusmod tempor incididunt.</p>
    </div>
  </div>
</section>

<section class="feature" style="top:1760px;height:540px">
  <div class="feature-photo" style="left:0;width:590px" role="img" aria-label="Photo of a businessman shaking hands across a desk"></div>
  <div class="feature-panel" style="left:590px;width:610px;padding-top:110px">
    <h2>Find talent to get<br>more done</h2>
    <ul class="tick-list">
      <li><span class="tick"><svg width="18" height="18" viewBox="0 0 18 18"><path d="M3 9l4 4 8-8" stroke="#fff" stroke-width="2.5" fill="none"/></svg></span><p>Lorem ipsum dolor sit amet, consectetur adipiscing elit,<br>sed do eiusmod tempor incididunt.</p></li>
      <li><span class="tick"><svg width="18" height="18" viewBox="0 0 18 18"><path d="M3 9l4 4 8-8" stroke="#fff" stroke-width="2.5" fill="none"/></svg></span><p>Lorem ipsum dolor sit amet, consectetur adipiscing elit,<br>sed do eiusmod tempor incididunt.</p></li>
      <li><span class="tick"><svg width="18" height="18" viewBox="0 0 18 18"><path d="M3 9l4 4 8-8" stroke="#fff" stroke-width="2.5" fill="none"/></svg></span><p>Lorem ipsum dolor sit amet, consectetur adipiscing elit,<br>sed do eiusmod tempor incididunt.</p></li>
    </ul>
  </div>
</section>

<section class="feature" style="top:2320px;height:440px">
  <div class="feature-panel" style="left:0;width:600px;padding-top:30px">
    <h2>Consulting solutions to drive business impact</h2>
    <ul class="tick-list">
      <li><span class="tick"><svg width="18" height="18" viewBox="0 0 18 18"><path d="M3 9l4 4 8-8" stroke="#fff" stroke-width="2.5" fill="none"/></svg></span><p>Lorem ipsum dolor sit amet, consectetur adipiscing elit,<br>sed do eiusmod tempor incididunt.</p></li>
      <li><span class="tick"><svg width="18" height="18" viewBox="0 0 18 18"><path d="M3 9l4 4 8-8" stroke="#fff" stroke-width="2.5" fill="none"/></svg></span><p>Lorem ipsum dolor sit amet, consectetur adipiscing elit,<br>sed do eiusmod tempor incididunt.</p></li>
      <li><span class="tick"><svg width="18" height="18" viewBox="0 0 18 18"><path d="M3 9l4 4 8-8" stroke="#fff" stroke-width="2.5" fill="none"/></svg></span><p>Lorem ipsum dolor sit amet, consectetur adipiscing elit,<br>sed do eiusmod tempor incididunt.</p></li>
    </ul>
  </div>
  <div class="feature-photo" style="left:600px;width:600px" role="img" aria-label="Photo of a consultant shaking hands with a client"></div>
</section>

<section class="feature" style="top:2772px;height:445px">
  <div class="feature-photo" style="left:0;width:610px" role="img" aria-label="Photo of a candidate greeting an employer at a desk"></div>
  <div class="feature-panel" style="left:610px;width:590px;padding-top:40px">
    <h2>Make the career move<br>you want</h2>
    <ul class="tick-list">
      <li><span class="tick"><svg width="18" height="18" viewBox="0 0 18 18"><path d="M3 9l4 4 8-8" stroke="#fff" stroke-width="2.5" fill="none"/></svg></span><p>Lorem ipsum dolor sit amet, consectetur adipiscing elit,<br>sed do eiusmod tempor incididunt.</p></li>
      <li><span class="tick"><svg width="18" height="18" viewBox="0 0 18 18"><path d="M3 9l4 4 8-8" stroke="#fff" stroke-width="2.5" fill="none"/></svg></span><p>Lorem ipsum dolor sit amet, consectetur adipiscing elit,<br>sed do eiusmod tempor incididunt.</p></li>
      <li><span class="tick"><svg width="18" height="18" viewBox="0 0 18 18"><path d="M3 9l4 4 8-8" stroke="#fff" stroke-width="2.5" fill="none"/></svg></span><p>Lorem ipsum dolor sit amet, consectetur adipiscing elit,<br>sed do eiusmod tempor incididunt.</p></li>
    </ul>
  </div>
</section>

<section class="trending">
  <h2>Trending job titles</h2>
  <div class="job-grid">
    <span class="job">Graphic Designer</span><span class="job">Graphic Designer</span><span class="job">Graphic Designer</span><span class="job">Graphic Designer</span>
    <span class="job">Digital Marketing</span><span class="job">Digital Marketing</span><span class="job">Digital Marketing</span><span class="job">Digital Marketing</span>
    <span class="job">UX Designer</span><span class="job">UX Designer</span><span class="job">UX Designer</span><span class="job">UX Designer</span>
  </div>
</section>

<section class="testimonials">
  <h2>What Client Says</h2>
  <svg class="quote" width="60" height="48" viewBox="0 0 60 48"><path d="M0 0h26v24L14 48H4l8-22H0zM34 0h26v24L48 48H38l8-22H34z" fill="#c8102e"/></svg>
  <blockquote>I had been searching for a new role for months with no luck until this team stepped in. They listened to what I wanted, matched me with a company that fits perfectly, and supported me at every stage. I could not be happier with the result.</blockquote>
  <div class="avatar" style="position:relative;display:block;margin:22px auto 0;width:52px;height:52px" role="img" aria-label="Client portrait"></div>
  <div class="client-name">Daniel K</div>
  <div class="avatar" style="left:20px;top:160px;width:56px;height:56px" role="img" aria-label="Client portrait"></div>
  <div class="avatar" style="left:120px;top:250px;width:56px;height:56px" role="img" aria-label="Client portrait"></div>
  <div class="avatar" style="left:18px;top:380px;width:56px;height:56px" role="img" aria-label="Client portrait"></div>
  <div class="avatar" style="left:1080px;top:170px;width:56px;height:56px" role="img" aria-label="Client portrait"></div>
  <div class="avatar" style="left:975px;top:250px;width:56px;height:56px" role="img" aria-label="Client portrait"></div>
  <div class="avatar" style="left:1080px;top:380px;width:56px;height:56px" role="img" aria-label="Client portrait"></div>
</section>

<section class="cta-band">
  <span class="cta-btn outline">Find your next job</span>
  <span class="cta-btn solid">Find your next hire</span>
</section>

<footer class="site-footer">
  <div class="footer-cols">
    <div class="footer-brand">
      <div class="brand"><span class="brand-mark"></span>Nuvara Talent</div>
      <p>Lorem ipsum dolor sit amet, consectetur adipiscing elit. Ut elit tellus, luctus nec ullamcorper mattis, pulvinar dapibus leo.</p>
      <div class="socials"><i></i><i></i><i></i></div>
    </div>
    <div class="footer-col">
      <h4>Useful Link</h4>
      <ul><li>About Us</li><li>Job List</li><li>FAQs</li><li>Team</li><li>Contact Us</li></ul>
    </div>
    <div class="footer-col">
      <h4>What We Do</h4>
      <ul><li>Recruitment</li><li>HR Outsourcing</li><li>Expatriate Services</li><li>Executive Search</li></ul>
    </div>
    <div class="subscribe">
      <h4>Subscribe &amp; Get Update Repeatedly</h4>
      <div class="field">Your Email</div>
      <span class="btn">Subscribe Now</span>
    </div>
  </div>
  <div class="copyright">© 2024, All Rights Reserved.</div>
</footer>

</body>
</html>
```